Honey jar label for small US farm

My daughters have 6 beehives and will be producing 300-400 jars of honey this season that they plan to sell at the farmers' market.
We are looking for a label design for small honey jars.
Label size:  1.5 inches high and 3 inches wide.
The label will be a simple RECTANGLE (no special cut)
We would like a playful look but upscale enough. We don't think that flowers or bees add anything. We like cleaner looks but not cold.
Maybe one could also represent the 3 sisters somewhere on the label. As elegant stick figures maybe?
One could also imagine a design where the label is black and the text/images are white to add some dramatic effect. The jar lid is black.
The honey is raw, un-pasturized, straight from the beehive.

Target Market(s)
Farm stand, sold by the 3 sisters who are 11, 9 and 6
Industry/Entity Type
Food Production
Colors
Designer to choose colors to be used in the design.
Requirements
Must have
- Name (means three sisters in English): Clos Ardent
- What it is: Berkshire Raw Honey
- Net weight: 3.75oz (110ml)
- Location: Richmond, MA
- Text on one of the sides: Sister to sister we will always be, a couple of nuts off the family tree!
- Note that the jar is an hexagon. See the attached STOCK photo.
- Therefore, a little more than 1 inch is on the front facing, and 0.75 inches on each sides.

Nice to have
- The design should be elegant (but not ornate), but clean. Inviting and fun.
- No need for bees or flowers which would not make it look upscale.
- No gold or "over the top" fancy. Modern but not cold.
- Remember that this is a honey brand for 3 young sisters. Something playful but upscale would work too.
- Not sure about color codes. We are quite happy staying in grey scales, but a little bit of colour might work too.

Should not have
- No UPC code needed

```html
<!DOCTYPE html>
<html lang="en">
<head>
<meta charset="utf-8">
<title>Clos Ardent — Berkshire Raw Honey label</title>
<link rel="stylesheet" href="https://fonts.googleapis.com/css2?family=Arimo:wght@400;700&family=Bebas+Neue&display=swap">
<style>
  :root {
    --page: #ebecec;
    --label: #2c2c2c;
    --comb-light: #343434;
    --comb-dark: #282828;
    --ink: #ffffff;
    --honey: #f5c900;
    --figures-top: #3a3a3a;
    --figures-bottom: #4a4a4a;
  }
  * { margin: 0; padding: 0; box-sizing: border-box; }
  html, body {
    width: 1200px;
    height: 647px;
    overflow: hidden;
    background: var(--page);
  }
  .label {
    position: absolute;
    left: 53px;
    top: 48px;
    width: 1093px;
    height: 549px;
    background: var(--label);
    font-family: "Arimo", Arial, sans-serif;
    color: var(--ink);
    overflow: hidden;
  }
  .comb-texture {
    position: absolute;
    inset: 0;
    background:
      radial-gradient(ellipse at 50% 45%, var(--comb-light) 0%, var(--label) 60%, var(--comb-dark) 100%);
  }
  .motto {
    position: absolute;
    left: 60px;
    top: 95px;
    width: 254px;
    text-align: center;
    font-size: 24px;
    line-height: 31px;
  }
  .brand {
    position: absolute;
    left: 385px;
    top: 112px;
    width: 320px;
    text-align: center;
    font-family: "Bebas Neue", sans-serif;
    font-weight: 400;
    font-size: 62px;
    line-height: 50px;
    letter-spacing: 9px;
    padding-left: 9px;
    color: var(--honey);
  }
  .product {
    position: absolute;
    left: 345px;
    top: 287px;
    width: 400px;
    text-align: center;
    font-family: "Bebas Neue", sans-serif;
    font-weight: 400;
    font-size: 38px;
    letter-spacing: 2px;
  }
  .dipper-art {
    position: absolute;
    left: 127px;
    top: 352px;
    width: 114px;
    height: 76px;
    border-radius: 18px;
    background: var(--honey);
  }
  .bee-art {
    position: absolute;
    left: 866px;
    top: 350px;
    width: 90px;
    height: 86px;
    border-radius: 20px;
    background: var(--honey);
  }
  .sisters-art {
    position: absolute;
    left: 437px;
    top: 364px;
    width: 222px;
    height: 80px;
    border-radius: 10px;
    background: linear-gradient(180deg, var(--figures-top), var(--figures-bottom));
  }
  .ground-arc {
    position: absolute;
    left: 393px;
    top: 440px;
    width: 304px;
    height: 32px;
  }
  .net-weight,
  .place {
    position: absolute;
    top: 505px;
    font-size: 23px;
    font-weight: 700;
    text-align: center;
  }
  .net-weight { left: 398px; width: 300px; }
  .place { left: 760px; width: 300px; }
</style>
</head>
<body>
  <main class="label">
    <div class="comb-texture" role="img" aria-label="Faint honeycomb hexagon pattern across the label"></div>

    <p class="motto">Sister to sister<br>we will always be,<br>a couple of nuts<br>off the family tree!</p>

    <h1 class="brand">Clos<br>Ardent</h1>

    <h2 class="product">Berkshire Raw Honey</h2>

    <div class="dipper-art" role="img" aria-label="Yellow honey dipper illustration"></div>

    <div class="sisters-art" role="img" aria-label="Line drawing of three little sisters dancing"></div>
    <svg class="ground-arc" viewBox="0 0 304 32" aria-hidden="true">
      <path d="M2 30 Q152 -6 302 30 Q152 10 2 30 Z" fill="var(--honey)"/>
    </svg>

    <div class="bee-art" role="img" aria-label="Yellow bee illustration"></div>

    <p class="net-weight">3.75oz (110ml)</p>
    <p class="place">Richmond, MA</p>
  </main>
</body>
</html>
```